2 Funky Pages + EASY stock logo = Construction Website

We would like a funky new website - Just 2 pages - to promote our project management company. A logo is also needed, but we'll provide a stock image which just needs a colour change a text added.

Here are the instructions:

"Hollow Fern Builders"

#logo
The one I'd like is attached. Please change font and positioning of text though.

Tagline is "Don't be normal - Be clever"

#Colour combo
756897 Wood Veneer
D5D6D2 sand dollar
353C3F charcoal
962715 brick red

#Home - Page 1

Our cost-price home build service will save you thousands.
No, seriously - Here's how we do it (button)

- Pay what the home building companies do.
- HFB will manage the entire project.
- Use Stonequay Guaranteed builders and materials.
- Tender for the best industry rates.
- Get a full budget calculated for the build.
- Avoid inflated 'Fixed-price' builds.
See how it works (button)

Contact Us: 0800 617 280
enquire - Name, Phone, email, comment - SEND

#How it works - Page 2

Traditional fixed price contracts are popular because it means that any risk of unexpected problems is carried by the home builder, but the builder will generally load the price about 10 times above the actual risk carried.

It's like an over-priced insurance policy, on steroids.

Clever people do things differently.

Here's how a cost-price build works...

1) Tell us what you want to build. Dream home, townhouse, investment property, whatever.

2) We'll put a design together for you, or you can choose from a bunch of plans we've already got.

3) We'll give you a conservative price estimate.

4) We finish tweaking your plans, then send them out to our network of more than 200 builders, subcontractors and tradesmen.

5) We collect the quotes, pick the best prices, and finalise your budget. Now you buy us beer, cause you've finally realised how much you're saving.

6) Tell your friends how awesome we are, while we lodge your building consent application with Council.

7) We coordinate the builders and subbies (look, you're already speaking trade-talk) from start to finish. You pay the cost price on their work each month.

We're happy to talk numbers and give you an estimate.

Contact Us: 0800 617 280

Reason: I have seen some great design elements, but need them to come together in one site design. Also, there appears to be less attention paid to the second page design ('how it works') than is necessary... There is no viable contender there yet, compared with the great home page submissions. I've also added some further info to the brief, and note that many submissions have ignored the colour combo I've requested.

Industry/Entity Type

Construction

Number of Pages Required

2 page

Requirements
Must have
• Stonequayer logo (small)
• Colour combo described in brief.
Nice to have
• I've attached a stock image I like, but it's certainly not essential. I do like images with clear backgrounds though - they tend to produce a crisp looking site.
• There is a wider image similar to this, available on Vorlin Imagery, but Pitchwell Hub won't let me attach it.
Should not have
• Photos of cheesy American faces.

```html
<!DOCTYPE html>
<html lang="en">
<head>
<meta charset="utf-8">
<title>Hollow Fern Builders</title>
<link rel="stylesheet" href="https://fonts.googleapis.com/css2?family=Oswald:wght@300;400&family=Arimo&display=swap">
<style>
:root{
  --sand:#d5d6d2;
  --veneer:#756897;
  --charcoal:#353c3f;
  --brick:#962715;
  --stone:#a8aaa3;
  --tile-brown:#9a6633;
  --tile-mauve:#976462;
  --tile-tan:#cd9966;
  --tile-olive:#999966;
  --white:#ffffff;
}
*{box-sizing:border-box;margin:0;padding:0}
html,body{width:1164px;height:1200px;overflow:hidden}
body{background:var(--sand);font-family:"Oswald",sans-serif;color:var(--white);position:relative;text-transform:uppercase}
.site-header{position:absolute;top:0;left:0;width:1164px;height:227px;background:var(--sand);text-align:center}
.brand{position:absolute;top:70px;left:0;width:100%;display:flex;justify-content:center;align-items:center;gap:14px}
.brand-mark{width:26px;height:26px;background:var(--brick)}
.brand-name{font-weight:400;font-size:34px;color:var(--brick);letter-spacing:1px}
.tagline{position:absolute;top:188px;left:0;width:100%;font-size:22px;font-weight:300;color:var(--charcoal);letter-spacing:1px}
.hero{position:absolute;top:227px;left:0;width:1164px;height:313px;border-top:3px solid var(--white);border-bottom:3px solid var(--white);text-align:center}
.hero-photo{position:absolute;inset:0;background:linear-gradient(100deg,#8a6a4a 0%,#b08468 35%,#c7946c 55%,#a07a62 75%,#8a7060 100%)}
.hero-title{position:relative;top:70px;font-size:24px;font-weight:400;line-height:37px;letter-spacing:1.5px}
.btn{display:inline-block;width:226px;height:44px;line-height:40px;background:var(--veneer);border:2px solid var(--white);font-family:"Oswald",sans-serif;color:var(--white);font-size:15px;letter-spacing:1px;text-transform:uppercase;text-align:center}
.hero .btn{position:absolute;left:442px;top:184px}
.benefits{position:absolute;top:540px;left:105px;width:951px;display:grid;grid-template-columns:repeat(3,317px);grid-template-rows:124px 131px}
.benefit{display:flex;align-items:center;justify-content:center;text-align:center;font-size:15px;line-height:25px;letter-spacing:1px;padding:0 10px}
.benefit b{font-size:18px;font-weight:400}
.benefit--brown{background:var(--tile-brown)}
.benefit--mauve{background:var(--tile-mauve)}
.benefit--tan{background:var(--tile-tan)}
.benefit--olive{background:var(--tile-olive)}
.benefits-cta{position:absolute;left:442px;top:807px}
.contact{position:absolute;top:863px;left:0;width:1164px;height:297px;background:var(--stone)}
.field{position:absolute;left:386px;width:355px;height:26px;background:var(--white);border:1px solid #8d8f88;font-family:"Arimo",sans-serif;font-size:11px;color:#777;padding:6px 9px;text-transform:uppercase}
.field--name{top:11px}.field--phone{top:52px}.field--email{top:91px}
.field--comment{top:130px;height:98px}
.contact .btn{position:absolute;left:450px;top:243px;height:43px}
.contact-info{position:absolute;left:760px;top:60px;width:190px;text-align:center;color:var(--charcoal)}
.contact-label{font-size:23px;font-weight:400;letter-spacing:1.5px}
.contact-phone{font-size:30px;font-weight:400;letter-spacing:2px;margin-top:10px}
.site-footer{position:absolute;top:1160px;left:0;width:1164px;height:40px;background:var(--charcoal);text-align:center;line-height:40px;font-family:"Arimo",sans-serif;font-size:11px;letter-spacing:.5px}
</style>
</head>
<body>
<header class="site-header">
  <div class="brand"><span class="brand-mark"></span><span class="brand-name">Hollow Fern Builders</span></div>
  <p class="tagline">Don't be normal - Be clever</p>
</header>

<section class="hero">
  <div class="hero-photo" role="img" aria-label="Soft-focus photo of a brick house among trees"></div>
  <h1 class="hero-title">Our cost-price home build service will<br>save you thousands.No, seriously</h1>
  <a class="btn" href="#">Here's how we do it</a>
</section>

<section class="benefits">
  <div class="benefit benefit--brown"><p><b>Pay</b> what the home<br>building companies do.</p></div>
  <div class="benefit benefit--mauve"><p>HFB will <b>manage</b> the entire project.</p></div>
  <div class="benefit benefit--brown"><p>Use <b>Stonequay</b><br>guaranteed builders and materials.</p></div>
  <div class="benefit benefit--tan"><p>Tender for the<br><b>best industry rates.</b></p></div>
  <div class="benefit benefit--brown"><p>Get a <b>full budget</b><br>calculated for the build.</p></div>
  <div class="benefit benefit--olive"><p>Avoid inflated<br><b>'Fixed-price'</b><br>builds.</p></div>
</section>
<a class="btn benefits-cta" href="#">Here's how we do it</a>

<section class="contact">
  <div class="field field--name">Name</div>
  <div class="field field--phone">Phone</div>
  <div class="field field--email">Email</div>
  <div class="field field--comment">Comment</div>
  <a class="btn" href="#">Send</a>
  <div class="contact-info">
    <p class="contact-label">Contact us</p>
    <p class="contact-phone">0800 617 280</p>
  </div>
</section>

<footer class="site-footer">Hollow Fern Builders © 2016</footer>
</body>
</html>
```